In Store POP Material Design

From: Derek Hollis
Sent: Wednesday, October 10, 2012 7:35 AM
To: 'Neil Carver'
Subject: Marketing Brief for K7 branding
We are looking to create a new look and feel for our Steadfast Coverage (k7) branded materials.
We sell extended service plans through retailers and manufacturers throughout North America.
The store sales personnel offer an extended warranty with the purchase of an Appliance, TV, computer, Camera etc.
We also want these materials to allow for us to include client logos so that we can leverage their brands to add value. I have included our old K7 brochure, a new concept for our Brixwell store clients and another client named Oxbow as reference
Our objective is to create in store tools (brochures, posters, stickers) etc to help the sales people close more sales. We are positioning our protection plans as part of a "total solution" sale. For example, if you buy a TV, you would also need to buy a mount, HDMI cable, screen cleaner etc. In our materials we want to illustrate this and help the sales person not only sell our warranty but the other accessories and services as well.
We also want to create a standard look and feel that is very info-graphic in nature. Heavy use of icons and a web 2.0 type of feel.
Have a look at some of these Infographics and you'll get an idea what I mean.
http://chartplume.example/wp-content/uploads/2012/05/HDTV-Comparison-LCD-vs.-Plasma.jpg
http://visualmarrow.example/wp-content/uploads/2011/04/Handset_Infographic_800px.jpg
My favorite sites are
http://www.graphlantern.example/
http://www.quillpixel.example/
You can reference info on our programs through our corporate website:
http://www.thenq8venture.example/extended-warranty-solutions
Bottom line, we want to create a new look and feel for the K7 brand and then tie whatever we come up with into both online and in-store materials.
The winner of this design contest will have plenty of work through this project as well as our other companies which you will find at: www.thehollisfold.example
Derek Hollis
Hollis Fold of Companies | www.thehollisfold.example
Q8 Ventures | HFX Manufacturing | GateKeeper Assurance
T: 1.555.318.2094 | M: 1.555.467.8130
E: derek.hollis@thehollisfold.example

```html
<!DOCTYPE html>
<html lang="en">
<head>
<meta charset="utf-8">
<title>K7 Steadfast Coverage Plan – In-Store Brochure</title>
<link href="https://fonts.googleapis.com/css2?family=Open+Sans:wght@400;600;700&display=swap" rel="stylesheet">
<style>
  :root{
    --stage:#575757;
    --fold-mark:#8a8a8a;
    --sky:#29a8e0;
    --navy:#1c5aa6;
    --ink:#111111;
    --grey-band:#dcdcdc;
    --grey-text:#8a8a8a;
    --panel:#ffffff;
    --leaf:#3cb878;
    --leaf-soft:#8fd8a8;
    --magenta:#e3177f;
    --badge-green:#1f9e5a;
    --badge-blue:#1d6fb8;
  }
  *{margin:0;padding:0;box-sizing:border-box}
  html,body{width:1045px;height:1200px;overflow:hidden}
  body{background:var(--stage);font-family:"Open Sans",Arial,sans-serif;position:relative;color:var(--ink)}

  .fold-label{position:absolute;left:529px;color:var(--fold-mark);font-size:13px;font-weight:600;transform:translateX(-50%) rotate(-90deg)}
  .fold-label.top{top:60px}
  .fold-label.bottom{top:1115px}

  .brochure{position:absolute;left:86px;top:93px;width:886px;height:994px;background:var(--panel);display:flex}
  .panel{position:relative;width:443px;height:994px;overflow:hidden}
  .panel + .panel{border-left:2px dashed #c9c9c9}

  /* shared bottom band */
  .bottom-band{position:absolute;left:0;right:0;top:882px;height:112px;background:var(--sky)}

  /* brand lockup */
  .brand{display:flex;align-items:center;gap:12px;color:var(--ink);font-weight:600}
  .brand-dot{width:16px;height:16px;border-radius:50%;background:var(--sky);flex:none}
  .brand-name{line-height:1.05}

  /* ---------- cover-left: accessories panel ---------- */
  .top-band{position:absolute;left:0;right:0;top:0;height:183px;background:var(--sky)}
  .brand-oval{position:absolute;left:67px;top:70px;width:320px;height:167px;border-radius:50%;
    border:6px solid var(--navy);background:linear-gradient(180deg,#fafafa 0%,#cfd2d5 55%,#9ea3a8 100%);
    display:flex;align-items:center;justify-content:center}
  .brand-oval .brand-name{font-size:24px}

  .appliance{position:absolute;left:148px;top:341px;width:131px;height:223px;border-radius:4px;
    background:linear-gradient(180deg,#3a3a3a 0%,#bfc3c6 30%,#8e9397 70%,#d9dcde 100%)}
  .connector{position:absolute;stroke:#6b7b88;stroke-width:2;stroke-dasharray:2 4;fill:none}

  .accessory-icon{position:absolute;width:62px;height:62px}
  .accessory-label{position:absolute;font-size:17px;font-weight:700;line-height:1.2;color:var(--ink)}

  .tagline{position:absolute;left:32px;top:738px;line-height:1}
  .tagline .lead{font-size:36px;font-weight:400;display:block}
  .tagline .focus{font-size:52px;font-weight:700;color:var(--navy);display:block;margin:6px 0 4px}
  .tagline .tail{font-size:36px;font-weight:400;display:block;text-align:right;padding-right:0;width:383px}

  .phone{position:absolute;left:0;right:0;top:0;height:112px;display:flex;align-items:center;justify-content:center;gap:10px;color:#fff;font-size:40px;font-weight:700}
  .phone svg{width:38px;height:38px}

  /* ---------- cover-right: sale panel ---------- */
  .cover-brand{position:absolute;left:56px;top:60px}
  .cover-brand .brand-name{font-size:28px}
  .cover-brand .brand-dot{width:22px;height:22px}

  .grey-field{position:absolute;left:0;right:0;top:186px;height:696px;background:var(--grey-band)}
  .section-title{position:absolute;left:0;right:0;top:192px;text-align:center;font-size:32px;color:#8f8f8f;font-weight:400}
  .family-photo{position:absolute;left:53px;top:241px;width:390px;height:581px;
    background:linear-gradient(160deg,#f1efe9 0%,#d9d4c8 40%,#c6b9a4 70%,#e9e6df 100%)}

  .tag-string{position:absolute;left:0;top:0;width:443px;height:320px;pointer-events:none}
  .sale-tag{position:absolute;left:28px;top:268px;width:262px;height:170px;transform:rotate(-11deg);
    background:var(--sky);padding:12px;box-shadow:2px 3px 6px rgba(0,0,0,.25)}
  .sale-tag-inner{width:100%;height:100%;background:#fff;display:flex;flex-direction:column;align-items:center;justify-content:center;line-height:1.05}
  .sale-tag .title{color:var(--magenta);font-size:34px;font-weight:600}
  .sale-tag .sub{color:#444;font-size:20px;letter-spacing:2px;margin-top:6px}

  .extend-note{position:absolute;left:0;right:0;top:846px;text-align:center;font-size:18px;color:var(--grey-text)}
  .term-badges{position:absolute;left:0;right:0;top:0;height:112px;display:flex;align-items:center;justify-content:center;gap:12px}
  .term-badge{width:66px;height:66px;display:flex;align-items:center;justify-content:center}
  .term-badge.three{background:var(--badge-green)}
  .term-badge.four{background:var(--badge-blue)}
  .term-badge span{width:50px;height:50px;border:2px solid #fff;border-radius:50%;color:#fff;display:flex;flex-direction:column;align-items:center;justify-content:center;font-size:20px;font-weight:700;line-height:1}
  .term-badge small{font-size:9px;font-weight:400}
</style>
</head>
<body>
  <div class="fold-label top">fold</div>
  <div class="fold-label bottom">fold</div>

  <div class="brochure">
    <!-- accessories panel -->
    <section class="panel accessories">
      <div class="top-band"></div>
      <div class="brand-oval">
        <div class="brand"><span class="brand-dot"></span><span class="brand-name">K7 Steadfast<br>Coverage Plan</span></div>
      </div>

      <svg class="connector" style="left:0;top:0" width="443" height="700" viewBox="0 0 443 700">
        <line x1="212" y1="290" x2="212" y2="330"/>
        <line x1="90" y1="410" x2="140" y2="410"/>
        <line x1="290" y1="410" x2="345" y2="410"/>
        <line x1="110" y1="570" x2="140" y2="545"/>
        <line x1="290" y1="545" x2="330" y2="580"/>
      </svg>

      <div class="appliance" role="img" aria-label="Stainless steel electric range"></div>

      <svg class="accessory-icon" style="left:30px;top:350px" viewBox="0 0 62 62" role="img" aria-label="Filters icon">
        <rect x="8" y="40" width="46" height="14" fill="var(--leaf-soft)"/>
        <rect x="14" y="6" width="10" height="38" rx="4" fill="var(--leaf)" transform="rotate(25 19 25)"/>
        <rect x="34" y="6" width="10" height="38" rx="4" fill="var(--leaf)" transform="rotate(25 39 25)"/>
      </svg>
      <div class="accessory-label" style="left:25px;top:426px">Filters</div>

      <svg class="accessory-icon" style="left:342px;top:350px;width:72px" viewBox="0 0 72 62" role="img" aria-label="Delivery truck icon">
        <rect x="10" y="40" width="56" height="14" fill="var(--leaf-soft)"/>
        <rect x="14" y="14" width="34" height="24" fill="var(--leaf)"/>
        <path d="M48 20h10l8 9v9H48z" fill="var(--leaf)"/>
        <circle cx="24" cy="40" r="5" fill="#fff" stroke="var(--leaf)" stroke-width="3"/>
        <circle cx="56" cy="40" r="5" fill="#fff" stroke="var(--leaf)" stroke-width="3"/>
        <line x1="0" y1="20" x2="10" y2="20" stroke="var(--leaf)" stroke-width="2"/>
        <line x1="2" y1="27" x2="10" y2="27" stroke="var(--leaf)" stroke-width="2"/>
      </svg>
      <div class="accessory-label" style="left:339px;top:426px">Delivery</div>

      <svg class="accessory-icon" style="left:44px;top:536px;height:76px" viewBox="0 0 62 76" role="img" aria-label="Cleaning spray bottle icon">
        <rect x="6" y="60" width="50" height="14" fill="var(--leaf-soft)"/>
        <path d="M18 4h20l8 6-6 4h-6v8h4l6 14v30H16V36l6-14h4v-8z" fill="var(--leaf)"/>
      </svg>
      <div class="accessory-label" style="left:42px;top:618px">Cleaning<br>Products</div>

      <svg class="accessory-icon" style="left:328px;top:540px;height:72px" viewBox="0 0 62 72" role="img" aria-label="Tools icon">
        <rect x="6" y="56" width="50" height="14" fill="var(--leaf-soft)"/>
        <line x1="10" y1="50" x2="50" y2="12" stroke="var(--leaf)" stroke-width="6" stroke-linecap="round"/>
        <line x1="14" y1="14" x2="48" y2="46" stroke="var(--leaf)" stroke-width="5" stroke-linecap="round"/>
        <circle cx="50" cy="12" r="7" fill="none" stroke="var(--leaf)" stroke-width="4"/>
      </svg>
      <div class="accessory-label" style="left:318px;top:618px">Install &amp;<br>Removal</div>

      <div class="tagline">
        <span class="lead">Rapid</span>
        <span class="focus">RESPONSE</span>
        <span class="tail">Service</span>
      </div>

      <div class="bottom-band">
        <div class="phone">
          <svg viewBox="0 0 40 40" aria-hidden="true">
            <circle cx="20" cy="20" r="18" fill="none" stroke="#fff" stroke-width="3"/>
            <path d="M13 11l5 0 2 6-3 2c1 3 4 6 7 7l2-3 6 2v5c-10 1-20-9-19-19z" fill="#fff"/>
          </svg>
          <span>1-866-555-0142</span>
        </div>
      </div>
    </section>

    <!-- sale cover panel -->
    <section class="panel sale-cover">
      <div class="cover-brand">
        <div class="brand"><span class="brand-dot"></span><span class="brand-name">K7 Steadfast<br>Coverage Plan</span></div>
      </div>

      <div class="grey-field"></div>
      <div class="section-title">Extended Service</div>
      <div class="family-photo" role="img" aria-label="Parent with child on back loading a refrigerator in a bright kitchen"></div>

      <svg class="tag-string" viewBox="0 0 443 320" aria-hidden="true">
        <path d="M70 290 C50 200 60 150 70 140 C80 135 92 150 88 190 C84 240 90 270 96 286" fill="none" stroke="#e8e8e8" stroke-width="5"/>
        <path d="M70 290 C50 200 60 150 70 140 C80 135 92 150 88 190 C84 240 90 270 96 286" fill="none" stroke="#9a9a9a" stroke-width="1"/>
      </svg>
      <div class="sale-tag">
        <div class="sale-tag-inner">
          <span class="title">Total</span>
          <span class="title">Solution</span>
          <span class="sub">SALE</span>
        </div>
      </div>

      <div class="extend-note">Extend your warranty to:</div>

      <div class="bottom-band">
        <div class="term-badges">
          <div class="term-badge three"><span>3<small>years</small></span></div>
          <div class="term-badge four"><span>4<small>years</small></span></div>
        </div>
      </div>
    </section>
  </div>
</body>
</html>
```